Website for Torvik Capital

We need a new web design for a company based in Chicago called "Torvik Capital". TVK provides portfolio management and financial advice using primarily income oriented strategies, such as, dividend paying stocks and preferred stocks. Our niche is utilizing conservative option strategies to help generate income and minimize risk. We are looking for a clean-cut and streamline professional site that is both appealing and user friendly. We would like the main colors to be the dark blue and bright green of our logo. Depending on cost and ease, we may want a designer to give us the completed website, including the coding, etc.

Target Market(s)

20-80 year old affluent investors seeking portfolio management and investment advice.

Industry/Entity Type

Conservative

Requirements
Must have
• -our logo
-main tabs: home, about us, our philosophy, our services, investment strategy, compliance, contact us
-our phone number visible and conveniently placed on each page
Nice to have
• -conveniently placed login button for current clients
-conveniently placed "quick contact" box on home page with spaces for first name, last name, email, phone number, and a blank box for their question or comment
-check us out on Socialbook and Chirper logos/buttons
-we like the idea of rotating pictures on top of page, but we aren't sure whether or not we definitely want that
Should not have
• -no trees
-no clocks
-no timers
-no crowns
-no plants

```html
<!DOCTYPE html>
<html lang="en">
<head>
<meta charset="utf-8">
<title>Torvik Capital – About Us</title>
<link href="https://fonts.googleapis.com/css2?family=Arimo:ital,wght@0,400;0,700;1,400;1,700&family=Tinos:wght@400;700&display=swap" rel="stylesheet">
<style>
:root{
  --navy:#0b0b66;
  --navy-deep:#05054f;
  --green:#8cc43d;
  --green-dark:#6fae25;
  --band-top:#6f8dc4;
  --band-bottom:#173a86;
  --page-grey:#eeeeee;
  --text:#111111;
  --rule:#d6d8e4;
  --footer-head:#a9b4cc;
}
*{box-sizing:border-box;margin:0;padding:0}
html,body{width:1134px;height:1200px;overflow:hidden}
body{position:relative;background:var(--page-grey);font-family:"Tinos","Times New Roman",serif;color:var(--text)}
.abs{position:absolute}

/* header */
.top-rule{left:0;top:0;width:1134px;height:5px;background:var(--navy-deep)}
.header{left:0;top:5px;width:1134px;height:99px;background:#fff}
.brand{left:113px;top:36px;display:flex;align-items:center;gap:10px}
.brand-dot{width:26px;height:26px;border-radius:50%;background:var(--green)}
.brand-name{font-family:"Arimo",Arial,sans-serif;font-weight:700;font-size:27px;color:var(--navy);letter-spacing:.5px}
.client-bar{left:884px;top:5px;width:137px;height:22px;background:var(--navy-deep);border-radius:0 0 8px 8px;display:flex;align-items:center;padding-left:10px;gap:3px}
.login-btn{width:46px;height:15px;border-radius:4px;background:linear-gradient(#a9d85b,#6fae25);font-family:"Arimo",Arial,sans-serif;font-size:10px;color:#fff;text-align:center;line-height:15px;margin-right:3px}
.mini-icon{width:15px;height:15px;border-radius:2px;background:#3f77c4}
.mini-icon.mail{background:#e8e8ee}
.consult{right:180px;top:47px;font-family:"Arimo",Arial,sans-serif;font-style:italic;font-size:16px;color:var(--navy)}
.phone-big{right:179px;top:64px;font-family:"Arimo",Arial,sans-serif;font-weight:700;font-size:27px;color:var(--green-dark);letter-spacing:.5px}
.phone-icon{left:962px;top:50px}

/* backgrounds */
.band-upper{left:0;top:104px;width:1134px;height:298px;background:linear-gradient(var(--band-top),var(--band-bottom))}
.band-footer{left:0;top:931px;width:1134px;height:269px;background:linear-gradient(#6a87c0,#2d4e93 55%,#1c3a80)}

/* main panel */
.panel{left:113px;top:123px;width:908px;height:879px;background:#fff;border-radius:8px;box-shadow:0 1px 4px rgba(0,0,0,.25);overflow:hidden}
.nav{position:absolute;left:0;top:0;width:908px;height:43px;background:var(--navy-deep);display:flex}
.nav a{display:block;height:43px;line-height:43px;text-align:center;color:#fff;font-weight:700;font-size:15px;text-decoration:none;border-right:1px solid #2a2a80;position:relative}
.nav a:last-child{border-right:0}
.nav a.active::after{content:"";position:absolute;left:50%;bottom:-7px;margin-left:-6px;border:6px solid transparent;border-top:7px solid var(--navy-deep);border-bottom:0}
.hero{position:absolute;left:0;top:43px;width:908px;height:122px;background:linear-gradient(100deg,#cfe6f2 0%,#8cc8e2 30%,#e6f1f7 55%,#f4f7f9 100%)}
.hero-photo{position:absolute;right:0;top:0;width:320px;height:122px;background:linear-gradient(90deg,rgba(240,244,247,0),#d3d8df 35%,#b4bac4)}
.hero-title{position:absolute;left:64px;top:40px;font-family:"Arimo",Arial,sans-serif;font-weight:700;font-size:30px;color:var(--navy);letter-spacing:.3px}
.hero-sub{position:absolute;left:64px;top:74px;font-weight:700;font-size:18px;color:#111}

.content{position:absolute;left:20px;top:205px;width:606px}
.content h2{font-family:"Arimo",Arial,sans-serif;font-weight:700;font-size:24px;color:var(--navy);padding-bottom:4px;background:linear-gradient(90deg,var(--rule),rgba(214,216,228,0)) left bottom/100% 2px no-repeat;margin-bottom:16px}
.content p{font-size:14.6px;line-height:22.7px}
.content .section-2{margin-top:52px}
.building{float:right;width:208px;height:151px;border:1px solid #ddd;padding:3px;margin:-2px 0 10px 20px}
.building div{width:100%;height:100%;background:linear-gradient(#c9d9e8,#a3b8cd)}
.content .after{clear:both;padding-top:12px}

/* sidebar */
.side-box{position:absolute;left:656px;width:236px;border:1px solid #7cb334;background:linear-gradient(135deg,#8cc43d 0%,#a9d36c 55%,#d0e8ad 100%)}
.quick{top:203px;height:327px}
.agent{position:absolute;left:1px;top:8px;width:88px;height:120px;background:linear-gradient(#a9c97a,#8aae5c)}
.quick-lead{position:absolute;left:90px;top:20px;width:132px;font-family:"Arimo",Arial,sans-serif;font-style:italic;font-weight:700;font-size:13px;line-height:16px;color:var(--navy)}
.field{position:absolute;left:14px;width:208px;height:28px;background:#fff;border:1px solid #c7d9ae;font-family:"Arimo",Arial,sans-serif;font-size:12px;color:#999;padding:8px 7px}
.btn{position:absolute;left:14px;height:27px;border-radius:4px;background:linear-gradient(#3a4aa0,#0b0b66);border:1px solid #06063e;color:#fff;font-family:"Arimo",Arial,sans-serif;font-weight:700;font-size:14px;line-height:25px;padding-left:14px}
.news{top:546px;height:211px}
.news-title{position:absolute;left:14px;top:18px;display:flex;align-items:center;gap:6px;font-family:"Arimo",Arial,sans-serif;font-weight:700;font-size:20px;color:var(--navy)}
.news-text{position:absolute;left:14px;top:56px;width:215px;font-family:"Arimo",Arial,sans-serif;font-size:13.5px;line-height:18px;color:var(--navy)}

/* footer */
.foot-col{top:1026px;font-family:"Arimo",Arial,sans-serif;color:#fff;font-size:12px}
.foot-col h3{font-family:"Tinos","Times New Roman",serif;font-weight:700;font-size:19px;color:var(--footer-head);margin-bottom:10px;height:22px}
.foot-col ul{list-style:none}
.foot-col li{height:25.5px;line-height:21px;border-bottom:1px solid rgba(255,255,255,.55);display:flex;align-items:center;gap:8px}
.soc{width:14px;height:14px;border-radius:2px;background:#dfe8f5}
</style>
</head>
<body>
<div class="abs top-rule"></div>
<header class="abs header"></header>
<div class="abs brand"><span class="brand-dot"></span><span class="brand-name">Torvik Capital</span></div>
<div class="abs client-bar"><span class="login-btn">Login</span><span class="mini-icon"></span><span class="mini-icon"></span><span class="mini-icon"></span><span class="mini-icon mail"></span></div>
<div class="abs consult">Contact us today for a consultation</div>
<div class="abs phone-big">(312) 555-0148</div>
<svg class="abs phone-icon" width="58" height="40" viewBox="0 0 58 40" aria-label="Telephone">
  <path d="M4 12 Q29 -2 54 12 L50 19 L40 16 L39 10 Q29 7 19 10 L18 16 L8 19 Z" fill="#2a2a2a"/>
  <path d="M16 20 L42 20 L50 36 L8 36 Z" fill="#333"/>
  <circle cx="29" cy="28" r="6" fill="#bbb"/><circle cx="29" cy="28" r="2.5" fill="#333"/>
</svg>

<div class="abs band-upper"></div>
<div class="abs band-footer"></div>

<main class="abs panel">
  <nav class="nav">
    <a style="width:85px">Home</a>
    <a class="active" style="width:104px">About Us</a>
    <a style="width:147px">Our Philosophy</a>
    <a style="width:131px">Our Services</a>
    <a style="width:177px">Investment Strategy</a>
    <a style="width:123px">Compliance</a>
    <a style="width:141px">Contact Us</a>
  </nav>
  <section class="hero">
    <div class="hero-photo" role="img" aria-label="Photo of a smiling business team in suits"></div>
    <h1 class="hero-title">WHO WE ARE</h1>
    <p class="hero-sub">Lorem ipsum dolor sit amet, consectetur adipiscing elit.</p>
  </section>

  <article class="content">
    <h2>Mission Statement</h2>
    <p>Lorem ipsum dolor sit amet, consectetur adipiscing elit. Nunc malesuada erat ac diam euismod nec aliquet mauris facilisis. Nulla nulla velit, scelerisque a lobortis vel, rhoncus eu neque. Duis congue diam vitaeg diam sollicitudin vitae facilisis nulla iaculis. Sed a urna sit amet leo varius feugiat sed.</p>
    <h2 class="section-2">Torvik Capital</h2>
    <figure class="building"><div role="img" aria-label="Photo of a glass office building"></div></figure>
    <p>Maecenas laoreet commodo leo eget condimentum. Morbi pulvinar sagittis fringilla. Suspendisse justo elit, facilisis sed faucibus vel, euismod et mauris. Aliquam arcu lacus, imperdiet vitae bibendum a, auctor eget felis. Pellentesque sit amet nulla id metus varius vehicula. Duis ornare dui quis dui venenatis porta. Mauris molestie placerat luctus. Donec sit amet magna neque. Praesent dapibus est accumsan justo.</p>
    <p class="after">Nunc elit mauris, porta a rutrum id, dictum sit amet velit. Nunc metus diam, fringilla quis tristique et, tincidunt vel elit. Sed pellentesque molestie elit nec tempus. Sed posuere dignissim nibh a dignissim. Nulla facilisi. Donec nibh nunc, volutpat ut tristique commodo, tristique porta eros. Vivamus vitae mauris eget sapien viverra rutrum at non quam nam accumsan erat dolor ras quisd. Sed tincidunt urna ut lacus rhoncus vestibulum. Integer quis lectus id sapien sollicitudin tempor eget vitae purus. Nunc lectus lacus, consectetur id elementum dapibus, pharetra a mi. Quisque vestibulum lacus a justo sollicitudin sed rhoncus sem fringilla. Suspendisse pharetra risus nec magna hendrerit quis euismod massa placerat. Phasellus magna nulla, gravida ut tempus et gravida. Maecenas laoreet commodo leo eget condimentum. Morbi pulvinar sagittis fringilla. Suspendisse justo elit, facilisis sed faucibus vel, euismod et mauris. Aliquamas agnam arcu lacus, imperdiet vitae.</p>
  </article>

  <aside class="side-box quick">
    <div class="agent" role="img" aria-label="Photo of a customer service agent with headset"></div>
    <p class="quick-lead">If you have questions, fill out the form below and contact us today</p>
    <div class="field" style="top:97px">Name</div>
    <div class="field" style="top:130px">Email</div>
    <div class="field" style="top:163px">Phone</div>
    <div class="field" style="top:196px;height:84px">Comment</div>
    <div class="btn" style="top:286px;width:88px">Submit &#10140;</div>
  </aside>

  <aside class="side-box news">
    <div class="news-title">
      <svg width="24" height="20" viewBox="0 0 24 20" aria-label="Envelope"><rect x="1" y="3" width="22" height="15" rx="1" fill="#fff" stroke="#6d8fb8"/><path d="M1 4 L12 12 L23 4" fill="none" stroke="#6d8fb8" stroke-width="1.5"/></svg>
      Newsletter
    </div>
    <p class="news-text">Subscribe to receive our updates and latest insights by email.</p>
    <div class="field" style="top:98px">Name</div>
    <div class="field" style="top:131px">Email</div>
    <div class="btn" style="top:168px;width:91px">Sign Up &#10140;</div>
  </aside>
</main>

<footer>
  <div class="abs foot-col" style="left:114px;width:312px">
    <h3>Torvik Capital</h3>
    <ul>
      <li>2250 W Harbor Street Suite 1800 Chicago, IL 60612</li>
      <li>Phone: (312) 555-0148</li>
      <li>Email: info@torvikcapital.com</li>
      <li>©2013 Torvik Capital.</li>
    </ul>
  </div>
  <div class="abs foot-col" style="left:483px;width:156px">
    <h3>Sitemap</h3>
    <ul><li>Home</li><li>About Us</li><li>Our Philosophy</li><li>Our Services</li></ul>
  </div>
  <div class="abs foot-col" style="left:653px;width:156px">
    <h3></h3>
    <ul><li>Investment Strategy</li><li>Compliance</li><li>Contact Us</li><li>Term &amp; Conditions</li></ul>
  </div>
  <div class="abs foot-col" style="left:866px;width:156px">
    <h3>Connect</h3>
    <ul><li><span class="soc"></span>Socialbook</li><li><span class="soc"></span>Chirper</li><li><span class="soc"></span>ProLink</li></ul>
  </div>
</footer>
</body>
</html>
```